Simple elegant business card

General card for a fin and television director.
Just want name, email, phone and address.

Target Market(s)

Prospective employers

Industry/Entity Type

Business

Requirements
Must have
• As above
Nice to have
• Logo but not necessary.
Should not have
• Not too colourful or funky.
• Simplicity and elegance the way to go.

```html
<!DOCTYPE html>
<html lang="en">
<head>
<meta charset="utf-8">
<title>Nora Hale — Director</title>
<link rel="stylesheet" href="https://fonts.googleapis.com/css2?family=Arimo:wght@400;700&display=swap">
<style>
  :root {
    --paper: #f3f3f3;
    --ink: #111111;
    --reel-light: #d6d6d6;
    --reel-dark: #1a1a1a;
    --reel-red: #a30000;
    --reel-red-deep: #7e0000;
  }
  html, body {
    margin: 0;
    padding: 0;
    overflow: hidden;
    background: var(--paper);
  }
  .card {
    position: relative;
    width: 1200px;
    height: 686px;
    background: var(--paper);
    overflow: hidden;
    font-family: "Arimo", "Helvetica Neue", Arial, sans-serif;
  }
  .card__artwork {
    position: absolute;
    inset: 0;
    width: 1200px;
    height: 686px;
  }
  .card__contact {
    position: absolute;
    left: 815px;
    top: 44px;
    margin: 0;
    color: var(--ink);
    font-size: 37px;
    line-height: 38px;
    letter-spacing: -0.3px;
  }
  .card__contact p { margin: 0; }
  .card__surname { font-weight: 700; }
</style>
</head>
<body>
  <main class="card">
    <svg class="card__artwork" viewBox="0 0 1200 686" aria-hidden="false">
      <defs>
        <linearGradient id="reelDarkTone" x1="0" y1="0" x2="1" y2="1">
          <stop offset="0" stop-color="var(--reel-light)"/>
          <stop offset="1" stop-color="#9a9a9a"/>
        </linearGradient>
        <linearGradient id="reelRedTone" x1="0" y1="0" x2="1" y2="1">
          <stop offset="0" stop-color="var(--reel-red)"/>
          <stop offset="1" stop-color="var(--reel-red-deep)"/>
        </linearGradient>
      </defs>
      <polygon class="reel reel--monochrome" role="img"
               aria-label="Black film strip with light frames curving from the top edge down to the lower left"
               points="0,0 377,0 526,217 623,389 663,686 299,686 0,331"
               fill="url(#reelDarkTone)"/>
      <polygon class="reel reel--red" role="img"
               aria-label="Red film strip with light frames angled up toward the right"
               points="432,471 923,221 1149,686 646,686"
               fill="url(#reelRedTone)"/>
    </svg>

    <address class="card__contact">
      <p class="card__name">Nora <span class="card__surname">Hale</span></p>
      <p class="card__email">norahale@mymail.com</p>
      <p class="card__phone">+1 310 555 0142</p>
    </address>
  </main>
</body>
</html>
```